Kestrel Learning Consultancy needs a colourful yet professional website

I am looking for a clean, colourful yet professional website that will appeal to schools and families looking for training and consultancy for children with and without special needs. The company is called Kestrel Learning Consultancy. I would be open to stock images being used and I attach my logo in the files below which should complement the design of the website. My strap line is 'achieve believe succeed' A website which offers similar services that I like the menu layout of is www.tovamplex.com. I would initially be looking at 7 main title links of: Home, About, Services, Team/Careers, Events, Links, Contact Us. The services title should have a drop down menu linking to Parents, Schools, Training, Professional Development, Supervision. Each page would contain fixed text with stock images where appropriate, bar the Events page where it may be laid out differently to display separate course events coming up. A contact us form would be required under the relevant tab. Ideas of formats, templates, logo etc are attached below. I look forward to reviewing designs!

Target Market(s)

Families and Schools

Industry/Entity Type

Education

Coding

Coded - Design and coding required

Font styles to use
Sans Serif

Requirements
Must have
• Logo incorporated
• Easy to read font
• Easy to navigate
Should not have
• Ultra modern minimalist style
• Dark colours

```html
<!DOCTYPE html>
<html lang="en">
<head>
<meta charset="utf-8">
<title>Kestrel Learning Consultancy</title>
<link rel="stylesheet" href="https://fonts.googleapis.com/css2?family=Roboto:wght@400;500;700&family=Oswald:wght@400;500&family=Ubuntu:wght@400;500&display=swap">
<style>
:root{
  --green:#a5bf2e;
  --green-dark:#8fa822;
  --red:#c0111a;
  --tan:#b08d57;
  --ink:#333;
  --muted:#666;
  --page:#f4f6ea;
  --footer-dark:#262626;
}
*{box-sizing:border-box;margin:0;padding:0}
html,body{width:1200px;height:2273px;overflow:hidden}
body{position:relative;background:linear-gradient(#f7f8ef,#f1f4e2 60%,#eef2da);font-family:"Roboto",sans-serif;color:var(--ink)}
.abs{position:absolute}
.header-phone{left:91px;top:68px;display:flex;align-items:center;gap:16px;font-size:22px;color:#222}
.phone-badge{width:38px;height:38px;border:1px solid #d99;border-radius:50%;display:flex;align-items:center;justify-content:center}
.brand{left:450px;top:60px;width:300px;text-align:center;display:flex;align-items:center;justify-content:center;gap:10px}
.brand-mark{width:22px;height:22px;border-radius:50%;background:var(--green)}
.brand-name{font-family:"Ubuntu",sans-serif;font-weight:500;font-size:22px;color:#6b4a2b}
.header-contact{left:986px;top:70px;width:128px;height:40px;background:linear-gradient(var(--red),#a30d15);color:#fff;font-size:16px;display:flex;align-items:center;justify-content:center;border-radius:2px}
.main-nav{left:91px;top:162px;width:1023px;height:59px;background:linear-gradient(#b8cf45,var(--green));display:flex;align-items:center;font-size:16px;color:#fff;text-transform:uppercase}
.main-nav a{color:#fff;text-decoration:none;height:100%;display:flex;align-items:center;justify-content:center}
.main-nav .is-active{background:var(--red);width:120px}
.hero{left:91px;top:221px;width:1023px;height:555px;background:linear-gradient(110deg,#9fb7c8,#d8c4a8 40%,#6f8aa8 75%,#344a6a);box-shadow:0 18px 22px -14px rgba(0,0,0,.45)}
.hero-title{right:25px;top:370px;text-align:left;font-family:"Oswald",sans-serif;color:#fff}
.hero-title h1{font-size:50px;font-weight:400;line-height:1}
.hero-title p{font-size:25px;margin-top:6px}
.hero-arrows{left:55px;top:480px;display:flex;gap:2px}
.hero-arrows span{width:28px;height:34px;background:rgba(0,0,0,.55);color:#fff;display:flex;align-items:center;justify-content:center;font-size:18px}
.welcome{left:91px;top:826px;width:1023px;text-align:center}
.welcome h2{font-family:"Ubuntu",sans-serif;font-weight:500;font-size:24px;color:#3a3a3a;text-transform:uppercase}
.welcome h2 em,.section-title em{font-style:normal;color:var(--red)}
.welcome p{margin:18px auto 0;width:930px;font-size:13px;line-height:23px;color:var(--muted)}
.service{top:1033px;width:328px;height:209px;border-radius:4px;color:#fff;text-align:center;padding-top:83px;box-shadow:0 16px 18px -12px rgba(0,0,0,.45)}
.service h3{font-family:"Ubuntu",sans-serif;font-weight:500;font-size:17px;text-transform:uppercase}
.service p{font-size:9.5px;line-height:15px;margin:12px auto 0;width:270px}
.service .more{font-size:10px;margin-top:18px;display:block}
.service-icon{position:absolute;left:102px;top:-62px;width:124px;height:124px;border-radius:50%;background:#fff;display:flex;align-items:center;justify-content:center;box-shadow:0 0 0 2px rgba(0,0,0,.06)}
.s-green{left:91px;background:var(--green)}
.s-red{left:436px;background:var(--red)}
.s-tan{left:782px;background:var(--tan)}
.what-we-do{left:91px;top:1291px;width:1023px;height:285px;border:1px solid #bbb;background:linear-gradient(90deg,#fff,#eee);box-shadow:0 18px 20px -14px rgba(0,0,0,.45)}
.wwd-photo{left:0;top:0;width:517px;height:283px;background:linear-gradient(120deg,#9cc7e6,#f0c9a0 45%,#e4e08a 70%,#d95b4a)}
.wwd-copy{left:553px;top:34px;width:440px}
.section-title{font-family:"Ubuntu",sans-serif;font-weight:500;font-size:23px;color:#222;text-transform:uppercase}
.wwd-copy p{margin-top:18px;font-size:15.5px;line-height:25.5px;color:#777;text-align:justify}
.btn-green{display:inline-flex;width:117px;height:36px;margin-top:20px;background:var(--green);color:#fff;font-size:13px;align-items:center;justify-content:center;border-radius:2px}
.events{left:91px;top:1626px;width:1021px;height:254px;background:#fff;border:1px solid #ddd;box-shadow:0 4px 8px rgba(0,0,0,.15)}
.events .section-title{position:absolute;left:44px;top:26px;font-size:22px;font-weight:400}
.events-arrows{position:absolute;right:48px;top:24px;font-size:18px;letter-spacing:6px}
.event{position:absolute;top:77px;display:flex;gap:14px}
.event-photo{width:144px;height:144px;border-radius:50%;border:4px solid #fff;box-shadow:0 0 0 2px #ccc}
.event h4{font-size:13.5px;font-weight:500;color:#111;margin-top:10px}
.event .date{font-size:11px;color:var(--green);margin-top:8px}
.event p{font-size:11px;line-height:18px;color:#333;margin-top:7px;width:284px}
.event .more{font-size:11px;color:var(--red);margin-top:7px;display:block}
.site-footer{left:0;top:1938px;width:1200px;height:226px;background:var(--green);color:#fff}
.f-col{position:absolute;top:36px}
.f-col h5{font-family:"Ubuntu",sans-serif;font-weight:500;font-size:15px;text-transform:uppercase}
.f-col ul{list-style:none;margin-top:16px}
.f-col li{font-size:11.5px;line-height:24.5px}
.f-col li::before{content:"\25B8  ";font-size:9px}
.f-col p{font-size:11.5px;line-height:17px;margin-top:16px;color:#f4f7e2}
.newsletter-form{display:flex;margin-top:16px}
.newsletter-form span{width:148px;height:30px;background:#eee;color:#777;font-size:11px;padding:9px 12px}
.newsletter-form b{width:56px;height:30px;background:var(--red);font-weight:400;font-size:12px;display:flex;align-items:center;justify-content:center}
.social-round{display:flex;gap:18px;margin-top:16px}
.social-round i{width:32px;height:32px;border:1px solid #fff;border-radius:50%}
.bottom-bar{left:0;top:2164px;width:1200px;height:109px;background:var(--footer-dark);color:#fff}
.legal{position:absolute;left:95px;top:36px;font-size:14px}
.legal span{margin:0 8px}
.copyright{position:absolute;left:95px;top:66px;font-size:11px}
.social-square{position:absolute;left:950px;top:47px;display:flex;gap:8px}
.social-square i{width:34px;height:34px}
</style>
</head>
<body>

<div class="abs header-phone">
  <span class="phone-badge"><svg width="18" height="18" viewBox="0 0 24 24"><path d="M6.6 10.8a15 15 0 0 0 6.6 6.6l2.2-2.2c.3-.3.7-.4 1-.2 1.1.4 2.3.6 3.6.6.6 0 1 .4 1 1V20c0 .6-.4 1-1 1A17 17 0 0 1 3 4c0-.6.4-1 1-1h3.5c.6 0 1 .4 1 1 0 1.3.2 2.5.6 3.6.1.3 0 .7-.2 1z" fill="#c0111a"/></svg></span>
  1800 555 014
</div>

<div class="abs brand"><span class="brand-mark"></span><span class="brand-name">Kestrel Learning Consultancy</span></div>

<div class="abs header-contact">CONTACT</div>

<nav class="abs main-nav">
  <a class="is-active" href="#">Home</a>
  <a href="#" style="width:124px">About</a>
  <a href="#" style="width:136px">Services</a>
  <a href="#" style="width:188px">Team &amp; Careers</a>
  <a href="#" style="width:130px">Events</a>
  <a href="#" style="width:118px">Links</a>
  <a href="#" style="width:182px">Contact Us</a>
</nav>

<section class="abs hero" role="img" aria-label="Photo of a smiling schoolgirl drawing at a desk in a library">
  <div class="abs hero-arrows"><span>&#8249;</span><span>&#8250;</span></div>
  <div class="abs hero-title"><h1>KESTREL LEARNING</h1><p>Neque porro quisquam est qui dolorem</p></div>
</section>

<section class="abs welcome">
  <h2>Welcome to <em>Kestrel Learning Consultancy</em></h2>
  <p>Lorem ipsum dolor sit amet, consectetur adipiscing elit, sed do eiusmod tempor incididunt ut labore et dolore magna aliqua. Ut enim ad minim veniam, quis nostrud exercitation ullamco laboris nisi ut aliquip ex ea commodo consequat. Duis aute irure dolor in reprehenderit in voluptate velit esse cillum dolore eu fugiat nulla pariatur. Excepteur sint occaecat cupidatat non proident, sunt in culpa qui officia deserunt mollit anim id est laborum</p>
</section>

<article class="abs service s-green">
  <div class="service-icon"><svg width="54" height="46" viewBox="0 0 54 46"><path d="M27 2 2 24h7v20h14V31h8v13h14V24h7L40 12V4h-6v3z" fill="#a5bf2e"/></svg></div>
  <h3>In-Home Early Intervention</h3>
  <p>Lorem Ipsum has been the industry's standard dummy text ever since the 1500s, when an unknown printer took a galley of type and scrambled it to make a type specimen book.</p>
  <span class="more">Read More &raquo;</span>
</article>
<article class="abs service s-red">
  <div class="service-icon"><svg width="56" height="46" viewBox="0 0 56 46"><circle cx="28" cy="11" r="9" fill="#c0111a"/><circle cx="11" cy="16" r="7" fill="#c0111a"/><circle cx="45" cy="16" r="7" fill="#c0111a"/><path d="M14 46c0-14 6-22 14-22s14 8 14 22z" fill="#c0111a"/><path d="M0 44c0-11 4-18 11-18 3 0 5 1 7 3-3 4-5 9-5 15z M56 44c0-11-4-18-11-18-3 0-5 1-7 3 3 4 5 9 5 15z" fill="#c0111a"/></svg></div>
  <h3>Parent and Sibling Training</h3>
  <p>Lorem Ipsum has been the industry's standard dummy text ever since the 1500s, when an unknown printer took a galley of type and scrambled it to make a type specimen book.</p>
  <span class="more">Read More &raquo;</span>
</article>
<article class="abs service s-tan">
  <div class="service-icon"><svg width="56" height="50" viewBox="0 0 56 50"><g fill="#8a6a3a"><circle cx="20" cy="28" r="13"/><g stroke="#8a6a3a" stroke-width="6"><path d="M20 8v40M0 28h40M6 14l28 28M34 14 6 42"/></g><circle cx="42" cy="13" r="8"/><g stroke="#8a6a3a" stroke-width="4"><path d="M42 1v24M30 13h24M34 5l16 16M50 5 34 21"/></g></g><circle cx="20" cy="28" r="5" fill="#fff"/><circle cx="42" cy="13" r="3" fill="#fff"/></svg></div>
  <h3>Group Services</h3>
  <p>Lorem Ipsum has been the industry's standard dummy text ever since the 1500s, when an unknown printer took a galley of type and scrambled it to make a type specimen book.</p>
  <span class="more">Read More &raquo;</span>
</article>

<section class="abs what-we-do">
  <div class="abs wwd-photo" role="img" aria-label="Photo of smiling children drawing together in a classroom"></div>
  <div class="abs wwd-copy">
    <h2 class="section-title">What <em>We Do</em></h2>
    <p>Lorem Ipsum has been the industry's standard dummy text ever since the 1500s, when an unknown printer took a galley of type and scrambled it to make a type specimen book. It has survived not only five centuries, but also the leap into electronic typesetting, remaining essentially unchanged.</p>
    <span class="btn-green">VIEW MORE</span>
  </div>
</section>

<section class="abs events">
  <h2 class="section-title">Latest <em>Events</em></h2>
  <div class="events-arrows">&lsaquo;&rsaquo;</div>
  <div class="event" style="left:42px">
    <div class="event-photo" role="img" aria-label="Photo of a young girl at school" style="background:linear-gradient(#f2e3c8,#c89a6a)"></div>
    <div><h4>SIMPLY DUMMY TEXT</h4><div class="date">20/08/2016</div><p>Lorem Ipsum has been the industry's standard dummy text ever since the 1500s, when an unknown printer took a galley of type and scrambled it to make a type specimen book.</p><span class="more">Read More &gt;&gt;</span></div>
  </div>
  <div class="event" style="left:536px">
    <div class="event-photo" role="img" aria-label="Photo of a cheering group of children" style="background:linear-gradient(#eef2f6,#e07a4a 60%,#4a7ac0)"></div>
    <div><h4>SIMPLY DUMMY TEXT</h4><div class="date">20/08/2016</div><p>Lorem Ipsum has been the industry's standard dummy text ever since the 1500s, when an unknown printer took a galley of type and scrambled it to make a type specimen book.</p><span class="more">Read More &gt;&gt;</span></div>
  </div>
</section>

<footer class="abs site-footer">
  <div class="f-col" style="left:112px">
    <h5>Links</h5>
    <ul><li>Customer Support</li><li>Documentation</li><li>Resources</li><li>General FAQs</li><li>Shortcodes</li></ul>
  </div>
  <div class="f-col" style="left:323px;width:230px">
    <h5>Careers</h5>
    <p>Lorem Ipsum has been the industry's standard dummy text ever since the 1500s, when an unknown printer took</p>
    <p style="margin-top:8px">a galley of type and scrambled it to make a type specimen book. It has survived not only five centuries, but also the leap into electronic typeset-</p>
  </div>
  <div class="f-col" style="left:674px">
    <h5>Get in Touch</h5>
    <p>Address : 412 Larkfield Road,<br>Millbrook, NJ</p>
    <p>Phone : 201 555 0187</p>
    <p>Email : hello@kestrellearning.example</p>
  </div>
  <div class="f-col" style="left:929px">
    <h5>Newsletter</h5>
    <p style="width:200px">Your about us information would fit here nicely.</p>
    <div class="newsletter-form"><span>Email address</span><b>Submit</b></div>
    <div class="social-round"><i></i><i></i><i></i></div>
  </div>
</footer>

<div class="abs bottom-bar">
  <div class="legal">Privacy Policy<span>|</span>Terms of Use<span>|</span>About Us<span>|</span>Sitemap</div>
  <div class="copyright">Copyright &copy; 2016 All Rights</div>
  <div class="social-square"><i style="background:#29a9e1"></i><i style="background:#c4302b"></i><i style="background:#3b5998"></i><i style="background:#0e76a8"></i></div>
</div>

</body>
</html>
```